Sunscreen Package Design Modern SPF 50

Update current package design to a more modern design target women 16-40 Do not make it playful. MESA VISTA is home to movie stars and high income business people PalmSprings is one of the most desired vacation areas in the world. The sun shines 350 days a year. World class Tennis and Golf tournaments are held every year with the worlds top players attending these tournaments

Target Market(s)

Women

Industry/Entity Type

Skin Protection

Font styles to use
Sans Serif

Requirements
Must have
• The words MESA VISTA and KOVALINE

```html
<!DOCTYPE html>
<html lang="en">
<head>
<meta charset="utf-8">
<title>Mesa Vista KOVALINE – SPF 50 Tubes</title>
<link href="https://fonts.googleapis.com/css2?family=Marcellus&family=Montserrat:wght@400;500&display=swap" rel="stylesheet">
<style>
  :root {
    --bg-top: #bdbdbd;
    --bg-bottom: #f4f4f4;
  }
  html, body { margin: 0; padding: 0; overflow: hidden; }
  body { width: 1200px; height: 912px; background: linear-gradient(180deg, var(--bg-top) 0%, #dcdcdc 45%, var(--bg-bottom) 100%); position: relative; font-family: "Montserrat", sans-serif; }

  .tube { position: absolute; top: 200px; width: 214px; height: 512px; color: var(--text); }
  .tube svg.shape { position: absolute; inset: 0; }
  .tube .body-fill { fill: var(--body); }
  .tube .cap-fill { fill: var(--cap); }
  .tube .cap-window { fill: none; stroke: rgba(0,0,0,.25); stroke-width: 1.2; }

  .label { position: absolute; left: 0; width: 100%; text-align: center; white-space: nowrap; }
  .brand-place { top: 98px; font-family: "Marcellus", serif; font-size: 30px; line-height: 30px; letter-spacing: .5px; color: var(--title); }
  .brand-name { top: 167px; font-size: 11.5px; font-weight: 500; letter-spacing: 2.2px; color: var(--title); }
  .divider { position: absolute; left: 106.5px; top: 193px; width: 1px; height: 62px; background: var(--title); }
  .product-type { top: 266px; font-size: 8.3px; font-weight: 500; letter-spacing: 1.3px; line-height: 10.5px; color: var(--text); }
  .product-type .rule { display: inline-block; width: 15px; height: 1px; background: var(--spf); vertical-align: middle; margin: 0 3px; }
  .spf-label { top: 295px; font-size: 11px; letter-spacing: .8px; color: var(--spf); }
  .spf-value { top: 306px; font-family: "Marcellus", serif; font-size: 32px; color: var(--spf); }
  .claims { top: 349px; font-size: 6.4px; line-height: 12px; letter-spacing: .4px; color: var(--text); }
  .claims .wide { letter-spacing: 1.2px; }
  .volume { top: 413px; font-size: 7.2px; letter-spacing: .3px; color: var(--text); }

  .tube--sand  { left: 33px;  --body: #e2d7c8; --cap: #d3692f; --title: #2f2b29; --text: #4a4440; --spf: #cf6a3c; }
  .tube--stone { left: 265px; --body: #cbc2b6; --cap: #6a6358; --title: #7a7269; --text: #857c72; --spf: #857c72; }
  .tube--sky   { left: 490px; --body: #a7bcc8; --cap: #3d5571; --title: #596671; --text: #5d6a75; --spf: #5d7896; }
  .tube--sage  { left: 717px; --body: #a8b2a0; --cap: #4e6233; --title: #4f564c; --text: #555d51; --spf: #5f6a58; }
  .tube--slate { left: 940px; --body: #454a4f; --cap: #23262b; --title: #f3f1ee; --text: #ebe8e4; --spf: #d7703f; }
</style>
</head>
<body>

<div class="tube tube--sand">
  <svg class="shape" width="214" height="512" viewBox="0 0 214 512" aria-hidden="true">
    <path class="body-fill" d="M0,0 H214 L198,425 Q196,437 184,437 H30 Q18,437 16,425 Z"/>
    <path class="cap-fill" d="M48,437 H166 L163,500 Q162,510 150,510 H64 Q52,510 51,500 Z"/>
    <rect class="cap-window" x="90" y="455" width="34" height="22" rx="2"/>
  </svg>
  <div class="label brand-place">MESA<br>VISTA</div>
  <div class="label brand-name">KOVALINE</div>
  <div class="divider"></div>
  <div class="label product-type">LUXURY SUNSCREEN<br><span class="rule"></span>LOTION<span class="rule"></span></div>
  <div class="label spf-label">SPF</div>
  <div class="label spf-value">50</div>
  <div class="label claims">UVA + UVB PROTECTION<br><span class="wide">BROAD SPECTRUM</span><br>WATER RESISTANT (80 MINUTES)</div>
  <div class="label volume">3 FL OZ / 88 mL</div>
</div>

<div class="tube tube--stone">
  <svg class="shape" width="214" height="512" viewBox="0 0 214 512" aria-hidden="true">
    <path class="body-fill" d="M0,0 H214 L198,425 Q196,437 184,437 H30 Q18,437 16,425 Z"/>
    <path class="cap-fill" d="M48,437 H166 L163,500 Q162,510 150,510 H64 Q52,510 51,500 Z"/>
    <rect class="cap-window" x="90" y="455" width="34" height="22" rx="2"/>
  </svg>
  <div class="label brand-place">MESA<br>VISTA</div>
  <div class="label brand-name">KOVALINE</div>
  <div class="divider"></div>
  <div class="label product-type">LUXURY SUNSCREEN<br><span class="rule"></span>LOTION<span class="rule"></span></div>
  <div class="label spf-label">SPF</div>
  <div class="label spf-value">50</div>
  <div class="label claims">UVA + UVB PROTECTION<br><span class="wide">BROAD SPECTRUM</span><br>WATER RESISTANT (80 MINUTES)</div>
  <div class="label volume">3 FL OZ / 88 mL</div>
</div>

<div class="tube tube--sky">
  <svg class="shape" width="214" height="512" viewBox="0 0 214 512" aria-hidden="true">
    <path class="body-fill" d="M0,0 H214 L198,425 Q196,437 184,437 H30 Q18,437 16,425 Z"/>
    <path class="cap-fill" d="M48,437 H166 L163,500 Q162,510 150,510 H64 Q52,510 51,500 Z"/>
    <rect class="cap-window" x="90" y="455" width="34" height="22" rx="2"/>
  </svg>
  <div class="label brand-place">MESA<br>VISTA</div>
  <div class="label brand-name">KOVALINE</div>
  <div class="divider"></div>
  <div class="label product-type">LUXURY SUNSCREEN<br><span class="rule"></span>LOTION<span class="rule"></span></div>
  <div class="label spf-label">SPF</div>
  <div class="label spf-value">50</div>
  <div class="label claims">UVA + UVB PROTECTION<br><span class="wide">BROAD SPECTRUM</span><br>WATER RESISTANT (80 MINUTES)</div>
  <div class="label volume">3 FL OZ / 88 mL</div>
</div>

<div class="tube tube--sage">
  <svg class="shape" width="214" height="512" viewBox="0 0 214 512" aria-hidden="true">
    <path class="body-fill" d="M0,0 H214 L198,425 Q196,437 184,437 H30 Q18,437 16,425 Z"/>
    <path class="cap-fill" d="M48,437 H166 L163,500 Q162,510 150,510 H64 Q52,510 51,500 Z"/>
    <rect class="cap-window" x="90" y="455" width="34" height="22" rx="2"/>
  </svg>
  <div class="label brand-place">MESA<br>VISTA</div>
  <div class="label brand-name">KOVALINE</div>
  <div class="divider"></div>
  <div class="label product-type">LUXURY SUNSCREEN<br><span class="rule"></span>LOTION<span class="rule"></span></div>
  <div class="label spf-label">SPF</div>
  <div class="label spf-value">50</div>
  <div class="label claims">UVA + UVB PROTECTION<br><span class="wide">BROAD SPECTRUM</span><br>WATER RESISTANT (80 MINUTES)</div>
  <div class="label volume">3 FL OZ / 88 mL</div>
</div>

<div class="tube tube--slate">
  <svg class="shape" width="214" height="512" viewBox="0 0 214 512" aria-hidden="true">
    <path class="body-fill" d="M0,0 H214 L198,425 Q196,437 184,437 H30 Q18,437 16,425 Z"/>
    <path class="cap-fill" d="M48,437 H166 L163,500 Q162,510 150,510 H64 Q52,510 51,500 Z"/>
    <rect class="cap-window" x="90" y="455" width="34" height="22" rx="2"/>
  </svg>
  <div class="label brand-place">MESA<br>VISTA</div>
  <div class="label brand-name">KOVALINE</div>
  <div class="divider"></div>
  <div class="label product-type">LUXURY SUNSCREEN<br><span class="rule"></span>LOTION<span class="rule"></span></div>
  <div class="label spf-label">SPF</div>
  <div class="label spf-value">50</div>
  <div class="label claims">UVA + UVB PROTECTION<br><span class="wide">BROAD SPECTRUM</span><br>WATER RESISTANT (80 MINUTES)</div>
  <div class="label volume">3 FL OZ / 88 mL</div>
</div>

</body>
</html>
```